Lantern Hollow Coffee Company Label

I am in need of a label for my coffee brand. I've attached my logo, and the label I've composed in the past. This brand has not launched yet, but we will launch within the week. I'm trying to identify other label options. I am familiar with Adobe Illustrator, enough to design what I have. What I'd like is a logo that is scalable, meaning I can easily change the name of the coffee. For consistency I'd like all of my roasts to have the same label, just different names and descriptions. I've included specs for the label, I'll be using the 3x4 labels for 16 oz bags. When you submit your design please follow the specs. There needs to be my company name and address on the label, however I don't want it to take over the label.

Please reply with any questions or clarifications.

Thank you,

Jed

```html
<!DOCTYPE html>
<html lang="en">
<head>
<meta charset="utf-8">
<title>Lantern Hollow Coffee Co. – Open Highway Blend Label</title>
<link rel="stylesheet" href="https://fonts.googleapis.com/css2?family=Gelasio:ital,wght@0,500;1,400&family=PT+Sans:wght@400&display=swap">
<style>
  :root {
    --backdrop: #2d0204;
    --top-dark: #57301a;
    --top-light: #7b5436;
    --band: #552e16;
    --body-top: #8d6a4e;
    --body-bottom: #dfbd95;
    --gold: #b8884c;
    --ink: #5b3a22;
    --ink-dark: #4a2a14;
    --name-light: #e9e6e2;
    --mark: #d9d5d0;
    --road: #55301a;
  }
  * { margin: 0; padding: 0; box-sizing: border-box; }
  html, body {
    width: 1200px; height: 1200px; overflow: hidden;
    background: var(--backdrop);
  }
  .label {
    position: absolute; left: 180px; top: 39px;
    width: 840px; height: 1122px; overflow: hidden;
    background: linear-gradient(to bottom, var(--body-top) 408px, var(--body-bottom) 1000px);
    box-shadow: 0 12px 30px rgba(0,0,0,0.45);
  }
  .label-header {
    position: absolute; left: 0; top: 0; width: 840px; height: 315px;
    background: linear-gradient(to bottom, var(--top-dark), var(--top-light));
  }
  .brand-mark {
    position: absolute; left: 360px; top: 80px; width: 120px; height: 120px;
    border-radius: 50%; background: var(--mark);
  }
  .brand-name {
    position: absolute; left: 0; width: 840px; text-align: center;
    font-family: "Gelasio", serif; font-weight: 500; color: var(--name-light);
    letter-spacing: 1px;
  }
  .brand-name.primary { top: 218px; font-size: 36px; font-variant: small-caps; line-height: 40px; }
  .brand-name.secondary { top: 262px; font-size: 18px; letter-spacing: 3px; text-transform: uppercase; line-height: 22px; }
  .title-band {
    position: absolute; left: 0; top: 315px; width: 840px; height: 93px;
    background: var(--band);
    display: flex; align-items: center; justify-content: center;
  }
  .blend-name {
    font-family: "Gelasio", serif; font-weight: 500; font-size: 56px;
    font-variant: small-caps; color: var(--gold); letter-spacing: 2px;
  }
  .tagline {
    position: absolute; left: 0; top: 418px; width: 840px; text-align: center;
    font-family: "Gelasio", serif; font-style: italic; font-size: 31px;
    line-height: 36px; color: var(--ink);
  }
  .flavour-notes {
    position: absolute; left: 0; top: 510px; width: 840px; text-align: center;
    font-family: "PT Sans", sans-serif; font-size: 48px; line-height: 54px;
    font-variant: small-caps; color: var(--ink-dark);
  }
  .road-illustration {
    position: absolute; left: 112px; top: 736px; width: 615px; height: 386px;
    border-radius: 300px 300px 0 0 / 120px 120px 0 0;
    background: linear-gradient(to bottom, rgba(85,48,25,0.55), rgba(85,48,25,0.25));
  }
  .net-weight {
    position: absolute; left: 45px; top: 1058px;
    font-family: "PT Sans", sans-serif; font-size: 22px; color: var(--ink-dark);
  }
  .company-address {
    position: absolute; right: 24px; bottom: 14px; width: 150px; text-align: right;
    font-family: "PT Sans", sans-serif; font-size: 13px; line-height: 16px; color: var(--ink-dark);
  }
</style>
</head>
<body>
  <main class="label">
    <header class="label-header">
      <div class="brand-mark"></div>
      <div class="brand-name primary">Lantern Hollow</div>
      <div class="brand-name secondary">Coffee Co.</div>
    </header>
    <div class="title-band">
      <h1 class="blend-name">Open Highway Blend</h1>
    </div>
    <p class="tagline">Perfect for use as an espresso, or on it’s own.<br>Compliments your daily commute or road trip</p>
    <p class="flavour-notes">Balanced,<br>Carmelly&nbsp; sweet<br>Espresso strength</p>
    <div class="road-illustration" role="img" aria-label="Illustration of a winding brown road with a dashed gold centre line, curving around a cluster of roasted coffee beans"></div>
    <p class="net-weight">Net wt.16 oz.</p>
    <address class="company-address" style="font-style: normal;">Lantern Hollow Coffee Co.<br>482 Willow Bend Rd<br>Cedar Falls, OR 97000</address>
  </main>
</body>
</html>
```